Online travel site needs edgy website design

tripvane is the first Global Business Travel Website that provides the most comprehensive destination information tailored to suit the business traveller.

It is a ‘one click solution’ that offers direct access to all aspects of business travel, including general information on the city, accommodation and transportation options, economic and financial statistics, key business and services contacts, as well as leisure activities, entertainment suggestions, and listings for any personal needs.

Much more than a travel website, tripvane.com eliminates the need to buy multiple travel books or visit scores of websites. Most importantly, it is the only website that will cover such an extensive range of destinations around the world, while also featuring cities where information is really scarce. The user-friendly and consistent format for all destinations will allow the business traveller to easily navigate through more than 100 information pages on any destination.

tripvane will be simple to navigate, intuitive, unique in design, dynamic, and content rich providing a supreme user experience during navigation of the website.

The website will initially be English and is set to expand to more languages in the future.

A beta site with back-end database has been built - and now we need an edgy state of the art graphic design to reskin it.

LOOK & FEEL

Scope
The design of the site should reflect tripvane’s corporate and user centric philosophy with the following elements:

a. tripvane corporate image and branding
b. the promotion of each city destination
c. tripvane being the starting point of travel, while also a partner during travel
d. the subtle but powerful presence of advertising and sponsorship

All the above must derive from the design outline and elements that are going to be used.

Design Guidelines

Innovative and elegant design, minimalism, simplicity that permits the offering of the required information to be delivered in line with the values of Trust, Care, Discovery & Connection.

In addition:

1. The usability, navigation and the informative character of the corporate web site should not be compromised by the design.
2. The over-segmented pages and over-crowded content per page should be avoided.
3. The design should not only guide the user in an inviting way to the information required but also to intrigue them for further navigation.
4. Advertising space should be anticipated in line with the design character and DMQ standard ad sizes.
5. The use of photos / videos should also encouraged.

Key Elements

a. Branding/Logos
Throughout the website branding should be present as a “guarantee seal” for the content accuracy. Corporate logo should be placed on every page while branding should also characterise any content element and/or tool. Appendix contains the current brand guidelines. Should additional sub-logos be required for specific sections, these should be proposed.

b. Fonts
Provided your experience on the website design you are requested to propose alternative font types and sizes always taken into consideration the inviting and user friendly character that the new website should aspire to. The font type that will be proposed must be user friendly in English typography, but also could support other languages in the future.

Given the fact that the majority of the text in the website contains information and listing, the fonts and text layout should not strain and fatigue the reader.

c. SEO
The design should be friendly towards the search engines.

d. Colours
Colour is considered as an integral part of the brand identity. Tripvane.com corporate colours are orange and grey as per the Attached document reference guide.

Different tonalities of the brand colours, or colours in general, should be proposed and applied, guided always by the above described scope of Look & Feel.

e. Section Headings
As presented above, the site’s section headings (refer Overview of the Site.) The principle is to label the content following users’ needs and mindset. However, the label space should be flexible for changes. The labels should facilitate the user to understand the content they host. This is important and should be applied especially to informative content.

Another function that Headings should perform is that of promoting the website’s content, especially when this kind of content will make the user spend more time in the website. This category of Headings should be approached in a more creative and attractive way as to intrigue users to check the content hosted.

f. Icons
Icons are considered necessary in order to provide the user extra help to guide them to reach the information they need quick n’ easy. Icons not only contribute actively to the creation of an attractive look & feel but, most importantly, facilitate navigation and speed up the users’ familiarisation with the website too.

Therefore their design should be eye-catching, comprehensive and dynamic, in accordance to the new site’s colour coding and following the latest trends as these were defined by the look & feel of smart phones.

PIXELHIVE BRIEF REQUIREMENTS
Based on the above, please provide at least two (2) approaches for the following pages – this includes colour palette in line with logo, layout, fonts.

Initial submissions can just address Deliverable 1 & 2 to fine tune design before proceeding further.

Please refer sample screenshots separately attached from raw beta site for content – available for Deliverables 2 -6.

(REFER example sites we like for their creativity: http://www.brindle-studio.example.co.uk/#Background, http://www.rotaclarafestas.example.com.br/, http://pembrookweb.example.co.uk/ )

Deliverable 1: Landing /Home page
- Access log in –
o Free Account or via Workloop/Chatterbox etc
o Membership Access – Login
- How to use the site
- Allowance for video or animation
- Destination Selection
- Blog & Social media links

Deliverable 2: Destination Landing Page / Template
This is essentially a city guide template to be used for all cities throughout the site.

This page clearly depicts the four information sections
1. General
2. Business
3. Leisure
4. Personal

Also this page should include:
- Business News Feed
- Advertising & Sponsorship Spaces (according to DMQ Standards)
- Destination Time, Weather, FX rates (LIVE feeds)
- Tips

Deliverable 3: Follow the above format but show an Internal Content Page – text only with subheadings

Deliverable 4: Follow the above format but show an Internal Content Page – text and photos

Deliverable 5: Follow the above format but show an Internal Content Page – Listing Sections such as Restaurants (this must also include filter categories)

Deliverable 6: Follow the above format but show an Internal Content Page – Top 10 Experiences – this incorporates address and contact details, photo and sub-text

Deliverable 7: The Membership Landing Page which should include:
1. Intro
2. Advertising & Sponsorship Space
3. The four sections
4. Tips Section
Updates

Hi all - just to reiterate that we are open to different approaches in the design.  We only included the existing screen shots of the beta site to provide you with an idea of the content.  We definitely don't want to see anything similar.....we want it to be edgy yet simple and easy to navigate....we want to create an outstanding user experience!  Cheers Tripvane Team

Reason: Dear Designers - We are extending the period as have not had many submissions at all and want to provide more time. If you have already submitted, we will be in touch shortly with feedback. Thanks for your understanding Tripvane Team

Reason: We would like to give everyone more time so we can find the best and most preferred design.

Target Market(s)

TARGET MARKET
tripvane is a consumer focused website, offering a wide-range of easy-to-use and interactive platforms, for informative and commercial purposes, while also providing attractive and innovative advertising real-estate for potential business partners.

The target audience can be segmented as follows:

Primary Target: Professionals travelling on Business

They require up-to-date reliable information prior and during their travel, as well as facilitation to take action. They need an online Personal Assistant.

The personal characteristics of the primary target group are: busy life, tailored solutions, reliable sources, trusting, caring, and spoiled.
 
The website will have a membership option (for a small annual fee) which will provide customized information for their demographic and preferences. Sub target groups will include:
1. Business Men 40 years
3. Business Women 40 years
5. Business People with reduced mobility

Demographic & Travelling Profile of Business Travellers

• 92% of them use the internet as a source of info
• 54% are males, 38 years old
• 80% holds a college/university degree
• 68% is travelling mainly for leisure and annually 6 times per year
• 52% reserve their ticket through the internet
• 66% is travel internationally

Secondary Targets:

Executive PA’s
Executive personal assistants who need to plan their manager’s travel and provide support information for their trip.

Professionals travelling for Leisure and Partners
They have most probably used the website for their business travel, but consider it also useful for their leisure travel. The generic website, will include enough information to cover most of the leisure needs, as well as the requirements of their partners.

Direct Business-to-Business [B2B] Targets
The direct [B2B] targeted audience includes corporations that would like to use a white label solution for their staff, by using all available destinations or a selected number depending on their global network.

Business-to-Business [B2B] Targets
The [B2B] targeted audience is an indirect audience, for which tripvane promotes its services, and a key revenue stream. The B2B audience consists mainly of a diverse range of professional organisations targeting the business traveller (airlines, hotels, travel agencies, tourism authorities, entertainment companies, services, etc.) tripvane will be targeting these organisations to advertise on the site.
 
Desired Response from Target Groups

The desired response from the consumer targets is:
a) Recurrent use of website
b) Share content/experience with friends and social networking sites
c) Interact on the website’s Blog
d) Register for newsletters and offers
e) Subscribe to Membership
f) Be exposed to commercial advertisements on the website
g) Provide feedback (in the future) for services
h) Use (in the future) online services to purchase products and services
Competition

Industry/Entity Type

Travel

Requirements
Must have
• A clean crisp and professional appearance giving a sense of Trust and Reliability.
Should not have
• It should not look like every other run of the mill travel sites - Roomly.com, Wanderpost etc

```html
<!DOCTYPE html>
<html lang="en">
<head>
<meta charset="utf-8">
<title>tripvane – Business Travel</title>
<link href="https://fonts.googleapis.com/css2?family=Open+Sans:wght@400;600;700&family=Arimo:wght@400;700&display=swap" rel="stylesheet">
<style>
:root{
  --orange:#f57c00;
  --orange-soft:#f28b2a;
  --grey-dark:#333333;
  --grey-mid:#555555;
  --grey-text:#666666;
  --grey-light:#999999;
  --panel:#f4f4f4;
  --band:#ececec;
  --line:#dddddd;
  --white:#ffffff;
  --field:#2e2e2e;
}
*{margin:0;padding:0;box-sizing:border-box}
html,body{width:950px;height:1200px;overflow:hidden;background:var(--white)}
body{position:relative;font-family:"Open Sans",Arial,sans-serif;color:var(--grey-dark)}
.abs{position:absolute}

/* header */
.site-header{left:0;top:0;width:950px;height:84px;background:var(--white);border-bottom:2px solid #cfcfcf}
.brand{left:102px;top:20px;display:flex;align-items:center;gap:10px}
.brand-mark{width:44px;height:44px;background:var(--orange)}
.brand-name{font-size:40px;font-weight:600;color:var(--orange);line-height:1;letter-spacing:-1px}
.main-nav{left:422px;top:37px;display:flex;gap:0;font-size:10px;color:var(--grey-dark)}
.main-nav a{color:inherit;text-decoration:none;margin-right:25px}
.lang-btn{left:780px;top:33px;width:71px;height:23px;background:#e6e6e6;border:1px solid #d4d4d4;border-radius:2px;font-size:9.5px;display:flex;align-items:center;gap:5px;padding-left:6px;box-shadow:0 1px 2px rgba(0,0,0,.15)}
.lang-btn i{width:10px;height:10px;background:var(--orange);display:block;border-radius:2px}

/* hero */
.hero{left:0;top:85px;width:950px;height:352px;background:linear-gradient(160deg,#3b3e44 0%,#2a2b30 40%,#4a4348 70%,#30323a 100%)}
.search-box{left:280px;top:172px;width:377px;height:190px;background:rgba(235,235,235,.93);box-shadow:0 2px 6px rgba(0,0,0,.4)}
.search-title{left:0;top:0;width:377px;height:38px;background:var(--field);color:var(--orange);font-size:12px;font-weight:600;padding:13px 14px}
.field{height:24px;background:var(--field);color:#e6e6e6;font-size:12px;padding:3px 9px;border-radius:2px;display:flex;justify-content:space-between;align-items:center;box-shadow:0 1px 2px rgba(0,0,0,.4)}
.field svg{flex:none}
.check{left:20px;top:152px;display:flex;align-items:center;gap:11px;font-size:12px;color:var(--grey-dark)}
.check i{width:11px;height:11px;background:var(--field);display:block}
.search-btn{left:196px;top:139px;width:156px;height:38px;background:var(--field);padding:3px}
.search-btn span{display:block;width:100%;height:100%;background:var(--orange);color:#fff;font-size:12px;font-weight:700;text-align:center;line-height:32px}

/* services */
.services{left:0;top:437px;width:950px;height:271px;background:#f7f7f7}
.sec-bar{left:108px;top:34px;width:2px;height:32px;background:var(--orange)}
.sec-title{left:121px;top:28px;font-size:19px;color:var(--grey-dark)}
.sec-sub{left:122px;top:53px;font-size:11px;font-weight:600;color:var(--grey-dark)}
.tabs{left:107px;top:82px;width:166px}
.tab{height:38.5px;background:linear-gradient(#f0f0f0,#dcdcdc);border-bottom:1px solid #cfcfcf;display:flex;align-items:center;gap:14px;padding-left:12px;font-size:12.5px;color:var(--grey-dark);font-weight:600}
.tab.active{background:var(--orange);color:#fff}
.tab svg{flex:none}
.tab-body{left:273px;top:82px;width:335px;height:153px;background:#fff;border:1px solid #e2e2e2;padding:20px 17px 0 18px;font-size:10.4px;line-height:17.5px;color:var(--grey-text);font-family:Arimo,Arial,sans-serif}
.tab-body a{display:block;margin-top:10px;color:var(--orange);font-weight:600;text-decoration:underline;font-family:"Open Sans",Arial,sans-serif}
.login-title{left:631px;top:38px;font-size:19px;color:var(--grey-dark)}
.login-box{left:632px;top:82px;width:225px;height:153px;background:#f0f0f0;border:1px solid #e0e0e0;border-bottom:2px solid #d5d5d5;padding:12px 10px;font-size:10.5px;line-height:15px;color:var(--grey-mid)}
.login-input{margin-left:1px;margin-top:0;width:203px;height:22px;background:#fff;border:1px solid #d8d8d8;border-top:2px solid #cfcfcf;font-size:9px;color:#888;padding:3px 9px}
.login-btn{width:50px;height:20px;background:var(--orange-soft);color:#fff;font-size:10px;font-weight:700;text-align:center;line-height:20px}

/* destinations */
.hot{left:0;top:708px;width:950px;height:227px;background:var(--band);border-top:1px solid #e2e2e2}
.hot-rule{top:25px;height:1px;background:#d6d6d6}
.hot-title{left:0;width:950px;top:16px;text-align:center;font-size:16px;color:var(--grey-dark)}
.hot-arrow{top:18px}
.card{top:48px;width:175px}
.card-photo{width:175px;height:111px;background:#fff;padding:5px;box-shadow:0 1px 1px rgba(0,0,0,.12)}
.card-photo div{width:100%;height:100%}
.card h3{font-weight:400;font-size:12.5px;margin:8px 0 0 3px;color:var(--grey-dark)}
.card p{font-size:9px;color:var(--grey-light);margin:2px 0 0 4px;line-height:11.5px;font-family:Arimo,Arial,sans-serif}

/* footer */
.site-footer{left:0;top:935px;width:950px;height:265px;background:var(--grey-dark)}
.fcol{top:36px}
.fcol h4{font-size:15px;color:#8a8a8a;font-weight:600;margin-bottom:8px}
.fcol ul{list-style:none}
.fcol li{font-family:Arimo,Arial,sans-serif;font-size:11px;color:#fff;line-height:17.5px;display:flex;align-items:center;gap:7px}
.fcol li.gap{margin-top:17px}
.fcol .accent{color:var(--orange-soft)}
.soc{width:13px;height:13px;border-radius:2px;display:block}
.copyright{left:106px;top:229px;font-size:10.5px;color:#fff}
.lang-foot{left:762px;top:226px;font-size:12.5px;color:#fff;display:flex;align-items:center;gap:6px;font-family:Arimo,Arial,sans-serif}
</style>
</head>
<body>

<header class="site-header abs">
  <div class="brand abs"><span class="brand-mark"></span><span class="brand-name">tripvane</span></div>
  <nav class="main-nav abs"><a>Home</a><a>Destinations</a><a>Tours</a><a>Blogs</a><a>About Us</a><a>Contact</a></nav>
  <div class="lang-btn abs"><i></i>Language</div>
</header>

<section class="hero abs" role="img" aria-label="Night aerial view of a city skyline with lit streets">
</section>

<form class="search-box abs">
  <div class="search-title abs">Find Your Destinations Or Tours</div>
  <div class="field abs" style="left:15px;top:55px;width:158px">All Destinations
    <svg width="10" height="7" viewBox="0 0 10 7"><path d="M1 1l4 4 4-4" stroke="#e6e6e6" stroke-width="2" fill="none"/></svg></div>
  <div class="field abs" style="left:195px;top:55px;width:157px">Departures Date
    <svg width="10" height="10" viewBox="0 0 10 10"><rect x="0.5" y="1.5" width="9" height="8" fill="none" stroke="#777"/><rect x="0.5" y="1.5" width="9" height="2" fill="#777"/></svg></div>
  <div class="field abs" style="left:15px;top:96px;width:158px">All Types
    <svg width="10" height="7" viewBox="0 0 10 7"><path d="M1 1l4 4 4-4" stroke="#e6e6e6" stroke-width="2" fill="none"/></svg></div>
  <div class="field abs" style="left:195px;top:90px;width:157px">Arrival Date
    <svg width="10" height="10" viewBox="0 0 10 10"><rect x="0.5" y="1.5" width="9" height="8" fill="none" stroke="#777"/><rect x="0.5" y="1.5" width="9" height="2" fill="#777"/></svg></div>
  <div class="check abs"><i></i>Advanced Search</div>
  <div class="search-btn abs"><span>Search Tours</span></div>
</form>

<section class="services abs">
  <div class="sec-bar abs"></div>
  <h2 class="sec-title abs" style="font-weight:400">How to Use Us?</h2>
  <p class="sec-sub abs">Check our great services</p>

  <div class="tabs abs">
    <div class="tab active">
      <svg width="26" height="20" viewBox="0 0 26 20"><path d="M3 18l6-6 3 3M9 12l3-6 5 3 4-2M12 6l2 7 3 5" stroke="#fff" stroke-width="2.2" fill="none" stroke-linecap="round"/><circle cx="16" cy="3" r="2.2" fill="#fff"/></svg>
      Visa Service</div>
    <div class="tab">
      <svg width="30" height="12" viewBox="0 0 30 12"><path d="M1 7l27-3-2 3-22 2z M12 5l4-4h2l-2 4 M10 8l5 3h2l-3-3" fill="#444"/></svg>
      Flights Service</div>
    <div class="tab">
      <svg width="24" height="14" viewBox="0 0 24 14"><path d="M1 1v13M23 6v8M1 11h22M1 7h22" stroke="#444" stroke-width="2" fill="none"/><rect x="3" y="3" width="5" height="4" fill="#444"/></svg>
      Hotel Service</div>
    <div class="tab">
      <svg width="20" height="18" viewBox="0 0 20 18"><path d="M3 2l14 14M17 2L3 16" stroke="#444" stroke-width="2.4" stroke-linecap="round"/></svg>
      Other Services</div>
  </div>

  <div class="tab-body abs">
    Lorem Ipsum est simplement du faux texte employé dans la sition et la misen page avant impression. Le Lorem Ipsum est le faux texte standard de l'imprimerie depuis les années 1500, quand un peintre anonyme assembla ensemble des morceaux de texte pour réaliser un livre spécimen de polices
    <a>View Detail</a>
  </div>

  <h2 class="login-title abs" style="font-weight:400">Membership Login</h2>
  <div class="login-box abs">
    <p style="margin-bottom:12px">Lorem Ipsum est simplement du faux texte employé dans la sition et la misen page</p>
    <div class="login-input">email</div>
    <div class="login-input" style="margin-top:8px">password</div>
    <div class="login-btn" style="margin-top:12px">Login</div>
  </div>
</section>

<section class="hot abs">
  <div class="hot-rule abs" style="left:0;width:360px"></div>
  <div class="hot-rule abs" style="left:600px;width:350px"></div>
  <svg class="hot-arrow abs" style="left:372px" width="8" height="14" viewBox="0 0 8 14"><path d="M7 1L1 7l6 6" stroke="#bbb" stroke-width="1.5" fill="none"/></svg>
  <h2 class="hot-title abs" style="font-weight:400">Our Hot Destinations</h2>
  <svg class="hot-arrow abs" style="left:585px" width="8" height="14" viewBox="0 0 8 14"><path d="M1 1l6 6-6 6" stroke="#bbb" stroke-width="1.5" fill="none"/></svg>

  <article class="card abs" style="left:111px">
    <div class="card-photo"><div role="img" aria-label="Business team walking beside a private jet" style="background:linear-gradient(180deg,#aebfd0,#3a3d44)"></div></div>
    <h3>Lorem Ipsum dolor</h3><p>Lorem Ipsum est simplement du faux texte employé dans.</p>
  </article>
  <article class="card abs" style="left:296px">
    <div class="card-photo"><div role="img" aria-label="Travellers shaking hands on an airfield at sunset" style="background:linear-gradient(180deg,#b7aa97,#4a4540)"></div></div>
    <h3>Lorem Ipsum dolor</h3><p>Lorem Ipsum est simplement du faux texte employé dans.</p>
  </article>
  <article class="card abs" style="left:478px">
    <div class="card-photo"><div role="img" aria-label="Business traveller in an airport terminal" style="background:linear-gradient(180deg,#8e98a3,#2f3a44)"></div></div>
    <h3>Lorem Ipsum dolor</h3><p>Lorem Ipsum est simplement du faux texte employé dans.</p>
  </article>
  <article class="card abs" style="left:665px">
    <div class="card-photo"><div role="img" aria-label="Group of travellers with rolling luggage in a bright hall" style="background:linear-gradient(180deg,#e4e8ea,#6e7276)"></div></div>
    <h3>Lorem Ipsum dolor</h3><p>Lorem Ipsum est simplement du faux texte employé dans.</p>
  </article>
</section>

<footer class="site-footer abs">
  <div class="fcol abs" style="left:108px"><h4>Company</h4>
    <ul><li>About</li><li>Contact Us</li><li>Meet Our Team</li><li>Newsroom</li><li>Blog</li><li>Privacy Policy</li><li>Terms of Use</li></ul></div>
  <div class="fcol abs" style="left:282px"><h4>Help</h4>
    <ul><li>How It Works</li><li>Help Center</li><li>Getting Started</li><li>Community Guidelines</li><li>Is Home Swapping Safe?</li></ul></div>
  <div class="fcol abs" style="left:456px"><h4>Useful Links</h4>
    <ul><li>Pricing &amp; Benefits</li><li>Member Stories</li><li>Travel Resources</li><li>Known Issues</li>
    <li class="gap">Already a Member of</li><li>Tripvane ?</li><li class="accent">Get our Special Offer!</li></ul></div>
  <div class="fcol abs" style="left:631px"><h4>Follow Us</h4>
    <ul><li><i class="soc" style="background:#4a6aa5"></i>Chatterbox</li><li><i class="soc" style="background:#3fa8e0"></i>Chirpline</li><li><i class="soc" style="background:#d8443c"></i>Pinboardly</li><li><i class="soc" style="background:#222"></i>Circlespace</li></ul></div>
  <div class="fcol abs" style="left:761px"><h4>Get Started</h4>
    <ul><li>Not a Member yet?</li><li class="accent">Join Now!</li></ul></div>
  <p class="copyright abs">© Tripvane.com™ All Rights Reserved.</p>
  <div class="lang-foot abs">
    <svg width="14" height="14" viewBox="0 0 14 14"><circle cx="7" cy="7" r="6" fill="none" stroke="#fff" stroke-width="1.4"/><path d="M1 7h12M7 1c-3 3-3 9 0 12M7 1c3 3 3 9 0 12" stroke="#fff" stroke-width="1.1" fill="none"/></svg>
    English</div>
</footer>

</body>
</html>
```